ARC VOLLEY Business Card Project

I'd like to request a business card design for the new company I've launched.
The name of the company is "ARC VOLLEY" an indoor unmanned tennis practice facility.
We would like to see designs that use our brand identity color in the logo I've attached.
We hope to get the design with modern, luxurious and elegant tone and manner.
We hope the logo should not be too big.

Business card must have elements as below:
- Logo (One of the logos I've attached)
- Name (In Korean Text) : 박 서 윤
- Title (In Korean Text) : 대표
- Phone Number : 010-8472-3916
- Email Address : seoyun.park@arcvolley-example.co.kr
- Website : www.arcvolley-example.co.kr
- Instagram : arcvolley
- Address (In Korean text) : 경기도 용인시 수지구 풍덕천로 456 미래타워 5층 501호, 502호

Target Market(s)

Tennis amateurs in 20 to 40s

Industry/Entity Type

Sports, Hobby

Contact Information for Business Card

- Logo (One of the logos I've attached) - Name (In Korean Text) : 박 서 윤 - Title (In Korean Text) : 대표 - Phone Number : 010-8472-3916 - Email Address : seoyun.park@arcvolley-example.co.kr - Website : www.arcvolley-example.co.kr - Instagram : arcvolley - Address (In Korean text) : 경기도 용인시 수지구 풍덕천로 456 미래타워 5층 501호, 502호

Font styles to use
Sans Serif

Requirements
Must have
• Double sided
Nice to have
• Logo with intaglio or relief embossing
Should not have
• Logo should not be too big.

```html
<!DOCTYPE html>
<html lang="ko">
<head>
<meta charset="utf-8">
<title>ARC VOLLEY Business Card</title>
<link href="https://fonts.googleapis.com/css2?family=Cinzel:wght@400&family=Noto+Sans+KR:wght@400;500&family=Noto+Sans:wght@400&display=swap" rel="stylesheet">
<style>
  :root {
    --page-bg: #e9e6e0;
    --card-white: #ffffff;
    --brand-green: #2f5a3a;
    --brand-green-dark: #274d31;
    --brand-green-light: #3a6a47;
    --text-dark: #2b2b2b;
    --divider: #9a9a9a;
    --on-green: #f4f1ea;
  }
  * { margin: 0; padding: 0; box-sizing: border-box; }
  html, body {
    width: 900px;
    height: 1200px;
    overflow: hidden;
    background: var(--page-bg);
  }
  .canvas {
    position: relative;
    width: 900px;
    height: 1200px;
  }
  .card {
    position: absolute;
    left: 75px;
    width: 750px;
    height: 456px;
    border-radius: 30px;
    box-shadow: 0 10px 24px rgba(0, 0, 0, 0.28);
    overflow: hidden;
  }
  .card--front {
    top: 90px;
    background: var(--card-white);
  }
  .card--back {
    top: 645px;
    background: linear-gradient(135deg, var(--brand-green-light) 0%, var(--brand-green) 45%, var(--brand-green-dark) 100%);
  }
  .wordmark {
    font-family: "Cinzel", serif;
    font-weight: 400;
    letter-spacing: 1px;
    white-space: nowrap;
  }
  .card--front .wordmark {
    position: absolute;
    left: 40px;
    top: 44px;
    font-size: 42px;
    color: var(--brand-green);
  }
  .card--back .wordmark {
    position: absolute;
    left: 0;
    right: 0;
    top: 196px;
    text-align: center;
    font-size: 50px;
    color: var(--on-green);
  }
  .person {
    position: absolute;
    left: 36px;
    top: 300px;
    font-family: "Noto Sans KR", sans-serif;
  }
  .person__name {
    font-size: 20px;
    font-weight: 500;
    color: var(--text-dark);
    letter-spacing: 1px;
  }
  .person__title {
    margin-top: 4px;
    font-size: 18px;
    color: var(--brand-green);
  }
  .contact-divider {
    position: absolute;
    left: 160px;
    top: 290px;
    width: 1px;
    height: 124px;
    background: var(--divider);
  }
  .contact-list {
    position: absolute;
    left: 178px;
    top: 290px;
    list-style: none;
    font-family: "Noto Sans KR", "Noto Sans", sans-serif;
    font-size: 14px;
    color: var(--text-dark);
  }
  .contact-list li {
    display: flex;
    align-items: center;
    gap: 8px;
    height: 25px;
    white-space: nowrap;
  }
  .contact-list svg {
    width: 16px;
    height: 16px;
    flex: none;
  }
</style>
</head>
<body>
<main class="canvas">
  <section class="card card--front" aria-label="Business card front">
    <div class="wordmark">ARC VOLLEY</div>
    <div class="person">
      <p class="person__name">박 서 윤</p>
      <p class="person__title">대표</p>
    </div>
    <div class="contact-divider"></div>
    <ul class="contact-list">
      <li>
        <svg viewBox="0 0 16 16" aria-hidden="true">
          <circle cx="8" cy="8" r="7" fill="none" stroke="#2b2b2b" stroke-width="1"/>
          <path d="M5.6 4.4l1.2 1.5-.7.9c.5 1 1.2 1.8 2.3 2.4l.9-.7 1.5 1.2-.8 1.3c-2.6-.4-4.8-2.7-5.1-5.2z" fill="#2b2b2b"/>
        </svg>
        <span>010-8472-3916</span>
      </li>
      <li>
        <svg viewBox="0 0 16 16" aria-hidden="true">
          <circle cx="8" cy="8" r="7" fill="none" stroke="#2b2b2b" stroke-width="1"/>
          <rect x="4.3" y="5.3" width="7.4" height="5.4" fill="none" stroke="#2b2b2b" stroke-width="0.9"/>
          <path d="M4.3 5.3L8 8.3l3.7-3" fill="none" stroke="#2b2b2b" stroke-width="0.9"/>
        </svg>
        <span>seoyun.park@arcvolley-example.co.kr</span>
      </li>
      <li>
        <svg viewBox="0 0 16 16" aria-hidden="true">
          <circle cx="8" cy="8" r="7" fill="none" stroke="#2b2b2b" stroke-width="1"/>
          <ellipse cx="8" cy="8" rx="2.6" ry="4.6" fill="none" stroke="#2b2b2b" stroke-width="0.8"/>
          <path d="M3.4 8h9.2" stroke="#2b2b2b" stroke-width="0.8"/>
        </svg>
        <span>www.arcvolley-example.co.kr</span>
      </li>
      <li>
        <svg viewBox="0 0 16 16" aria-hidden="true">
          <circle cx="8" cy="8" r="7" fill="none" stroke="#2b2b2b" stroke-width="1"/>
          <circle cx="8" cy="8" r="2.4" fill="none" stroke="#2b2b2b" stroke-width="0.9"/>
        </svg>
        <span>arcvolley</span>
      </li>
      <li>
        <svg viewBox="0 0 16 16" aria-hidden="true">
          <circle cx="8" cy="8" r="7" fill="none" stroke="#2b2b2b" stroke-width="1"/>
          <path d="M8 12.2s-3-3.2-3-5.3a3 3 0 0 1 6 0c0 2.1-3 5.3-3 5.3z" fill="none" stroke="#2b2b2b" stroke-width="0.9"/>
          <circle cx="8" cy="6.9" r="1" fill="#2b2b2b"/>
        </svg>
        <span>경기도 용인시 수지구 풍덕천로 456 미래타워 5층 501호, 502호</span>
      </li>
    </ul>
  </section>

  <section class="card card--back" aria-label="Business card back">
    <div class="wordmark">ARC VOLLEY</div>
  </section>
</main>
</body>
</html>
```